Carpet cleaning company focused on high quality needs business cards

We are a growing company that just merged with another company and need to design a new business card. We do both residential as well as commercial cleaning. We do carpet, tile & grout, upholstery, hard floors, and stain & pet odor removal. We treat our customers like family and strive to achieve outstanding results with every job.

```html
<!DOCTYPE html>
<html lang="en">
<head>
<meta charset="utf-8">
<title>Hale's Fresh Crew Cleaning – Business Card</title>
<link href="https://fonts.googleapis.com/css2?family=Lato:wght@400;700;900&display=swap" rel="stylesheet">
<style>
  :root {
    --backdrop: #2b2b2b;
    --card: #ececec;
    --red: #d8413a;
    --blue: #1173ad;
    --gold: #b08a4e;
    --ink: #1d1d1d;
    --white: #ffffff;
  }
  * { margin: 0; padding: 0; box-sizing: border-box; }
  html, body {
    width: 1200px; height: 1200px; overflow: hidden;
    background: var(--backdrop);
    font-family: 'Lato', sans-serif;
  }
  .card {
    position: absolute;
    left: 201px;
    width: 797px; height: 455px;
    border-radius: 24px;
    background: var(--card);
    overflow: hidden;
  }
  .card--front { top: 96px; }
  .card--back { top: 656px; }

  .front-band { position: absolute; inset: 0; width: 100%; height: 100%; }

  .identity { position: absolute; left: 326px; top: 58px; }
  .identity__name {
    font-weight: 700; font-size: 50px; line-height: 1;
    color: var(--blue); letter-spacing: 0.5px;
  }
  .identity__title {
    margin-top: 6px;
    font-weight: 400; font-size: 23px; color: var(--gold);
    letter-spacing: 0.5px;
  }

  .contact { position: absolute; right: 72px; top: 222px; list-style: none; }
  .contact__item {
    display: flex; align-items: center; justify-content: flex-end;
    gap: 14px;
    color: var(--white); font-size: 19px; line-height: 26.5px;
  }
  .contact__item--gap { margin-top: 8px; }
  .contact__icon { width: 18px; height: 18px; flex: none; }

  .brand {
    position: absolute; left: 0; top: 0; width: 100%; height: 100%;
    display: flex; align-items: center; justify-content: center; gap: 26px;
  }
  .brand__mark { width: 118px; height: 118px; background: var(--red); flex: none; }
  .brand__name {
    font-weight: 900; font-size: 42px; line-height: 1.05;
    color: var(--ink); text-transform: uppercase;
  }
</style>
</head>
<body>

<section class="card card--front">
  <svg class="front-band" viewBox="0 0 797 455" preserveAspectRatio="none" aria-hidden="true">
    <polygon points="0,336 797,88 797,455 0,455" fill="var(--red)"/>
  </svg>

  <div class="identity">
    <h1 class="identity__name">MARK DELANEY</h1>
    <p class="identity__title">Founder &amp; CEO</p>
  </div>

  <ul class="contact">
    <li class="contact__item">4870 Birchwood Lane
      <svg class="contact__icon" viewBox="0 0 24 24"><path d="M12 2a7 7 0 0 0-7 7c0 5 7 13 7 13s7-8 7-13a7 7 0 0 0-7-7z" fill="none" stroke="#fff" stroke-width="2"/><circle cx="12" cy="9" r="2.5" fill="#fff"/></svg>
    </li>
    <li class="contact__item">Millbrook, CT 06099<span class="contact__icon"></span></li>
    <li class="contact__item contact__item--gap">(555) 014-2290
      <svg class="contact__icon" viewBox="0 0 24 24"><path d="M6 3l3 0 2 5-2 1.5a11 11 0 0 0 5.5 5.5L16 13l5 2v3a2 2 0 0 1-2 2A16 16 0 0 1 4 5a2 2 0 0 1 2-2z" fill="none" stroke="#fff" stroke-width="2" stroke-linejoin="round"/></svg>
    </li>
    <li class="contact__item">(555) 014-2290
      <svg class="contact__icon" viewBox="0 0 24 24"><rect x="6" y="2" width="12" height="20" rx="2" fill="none" stroke="#fff" stroke-width="2"/><circle cx="12" cy="18" r="1.2" fill="#fff"/></svg>
    </li>
    <li class="contact__item">hello@halesfreshcrew.com
      <svg class="contact__icon" viewBox="0 0 24 24"><rect x="2" y="5" width="20" height="14" fill="#fff"/><path d="M2 5l10 8 10-8" fill="none" stroke="var(--red)" stroke-width="1.6"/></svg>
    </li>
    <li class="contact__item">halesfreshcrew.com
      <svg class="contact__icon" viewBox="0 0 24 24"><circle cx="12" cy="12" r="9" fill="none" stroke="#fff" stroke-width="2"/><path d="M3 12h18M12 3c3 3 3 15 0 18M12 3c-3 3-3 15 0 18" fill="none" stroke="#fff" stroke-width="1.5"/></svg>
    </li>
  </ul>
</section>

<section class="card card--back">
  <div class="brand">
    <div class="brand__mark" aria-hidden="true"></div>
    <p class="brand__name">Hale's<br>Fresh Crew<br>Cleaning</p>
  </div>
</section>

</body>
</html>
```